business card design and letterhead for a building inspection company. We have a pre-purchase building and pest inspection ( i inspect house before people purchase it)
Updates

Tilda has been so so responsive and good, i highly recommend her

Industry/Entity Type

Building

Contact Information for Business Card

audience, solicitor, real estate agent, mortgage brokerthe rest of the info will be in the attachement business card

```html
<!DOCTYPE html>
<html lang="en">
<head>
<meta charset="utf-8">
<title>Keystone Homecheck – Business Card</title>
<link href="https://fonts.googleapis.com/css2?family=Open+Sans:wght@400;600;700&display=swap" rel="stylesheet">
<style>
  :root {
    --bg: #e4e5e7;
    --card: #ffffff;
    --blue: #1a76c1;
    --black: #0b0b0b;
    --ink: #3a3a3a;
    --white: #ffffff;
  }
  * { margin: 0; padding: 0; box-sizing: border-box; }
  html, body { width: 1200px; height: 883px; overflow: hidden; }
  body {
    background: var(--bg);
    font-family: "Open Sans", Arial, sans-serif;
    position: relative;
  }
  .card {
    position: absolute;
    width: 520px;
    height: 297px;
    background: var(--card);
    border-radius: 30px;
    overflow: hidden;
    box-shadow: 0 10px 30px rgba(0,0,0,0.12);
  }
  .card--back { left: 610px; top: 120px; }
  .card--front { left: 90px; top: 450px; }

  /* Back */
  .brand {
    position: absolute;
    left: 60px; top: 128px;
    display: flex; align-items: center; gap: 12px;
  }
  .brand__mark { width: 30px; height: 30px; background: var(--blue); flex: none; }
  .brand__name {
    color: var(--blue); font-weight: 700;
    font-size: 22px; line-height: 1; letter-spacing: 1px;
    white-space: nowrap;
  }
  .back-band {
    position: absolute; right: 0; top: 52px; height: 58px; width: 240px;
    display: flex;
  }
  .back-band__web {
    flex: 1; background: var(--blue); color: var(--white);
    font-size: 10px; letter-spacing: 1.5px;
    display: flex; align-items: center; justify-content: center;
  }
  .back-band__end { width: 62px; background: var(--black); }

  /* Front */
  .person {
    position: absolute; left: 200px; top: 44px; width: 260px; text-align: center;
    color: var(--ink);
  }
  .person__name { font-size: 24px; font-weight: 400; letter-spacing: 0.5px; line-height: 1.1; }
  .person__name b { font-weight: 700; }
  .person__role { font-size: 12px; margin-top: 2px; }
  .person__role b { font-weight: 700; }

  .front-accent {
    position: absolute; left: 0; top: 128px; width: 14px; height: 96px; background: var(--blue);
  }
  .phone-block {
    position: absolute; left: 14px; top: 128px; width: 206px; height: 96px;
    background: var(--black); color: var(--white);
    padding: 16px 0 0 68px; font-size: 15px; line-height: 1.25;
  }
  .web-block {
    position: absolute; left: 220px; top: 100px; right: 0; height: 98px;
    background: var(--blue); color: var(--white);
    padding: 20px 0 0 54px; font-size: 14px; line-height: 1.25; text-align: center;
  }
  .web-block__inner { display: inline-block; text-align: center; }
  .address {
    position: absolute; left: 190px; top: 236px; width: 280px; text-align: center;
    color: var(--ink); font-size: 12px; line-height: 1.3;
  }
  .address b { font-weight: 700; }
</style>
</head>
<body>

  <section class="card card--back" aria-label="Card back">
    <div class="brand">
      <span class="brand__mark"></span>
      <div class="brand__name">KEYSTONE HOMECHECK</div>
    </div>
    <div class="back-band">
      <div class="back-band__web">WWW.WEBDOMAIN.COM</div>
      <div class="back-band__end"></div>
    </div>
  </section>

  <section class="card card--front" aria-label="Card front">
    <div class="person">
      <div class="person__name">SARAH <b>TILDA</b></div>
      <div class="person__role"><b>SENIOR</b> GRAPHIC DESIGNER</div>
    </div>
    <div class="web-block">
      <div class="web-block__inner">
        EMAIL &amp; WEB<br>
        CONTACT@DOMAIN.COM<br>
        WWW.WEBDOMAIN.COM
      </div>
    </div>
    <div class="front-accent"></div>
    <div class="phone-block">
      PHONE &amp; FAX<br>
      +123 456 7890<br>
      +012 345 6789
    </div>
    <div class="address">
      217 <b>STREET</b> ADDRESS, YOUR <b>CITY 9700</b><br>
      <b>UNITED KINGDOM</b>
    </div>
  </section>

</body>
</html>
```